Volta Medica Innovative Business Card

Stunning business card. Background will be black. Letters in gold. Modern yet simple design that is attention grabbing. QR code leading to site. Attractive primarily to males ages 30 to 50 but also to females in same age range looking for beauty and mental health products

Target Market(s)

Males in the 30-50 age demographics

Industry/Entity Type

Pharmaceuticals selling erectile dysfunction and mens health medications

Contact Information for Business Card

www.voltamedica.example; (555) NOW-BOLT; info@voltamedica.example

Colors
FFC000
F8CF3A
FAE287
FDF2CF
FEFAEE

Requirements
Must have
• Black business card with gold letters.
Nice to have
• perhaps just the logo or the "R" icon by itself on one side
Should not have
• too much content so it does not look busy

```html
<!DOCTYPE html>
<html lang="en">
<head>
<meta charset="utf-8">
<title>Volta Medica Business Card</title>
<link rel="stylesheet" href="https://fonts.googleapis.com/css2?family=Montserrat:wght@800&family=Lato:wght@400&family=Arimo:wght@400&display=swap">
<style>
  :root {
    --page-bg: #161616;
    --card-front: #201c1c;
    --card-back: #1d1c1b;
    --gold-line: #c9a23a;
    --gold-text: #e2bd45;
    --gold-bright: #f8cf3a;
  }
  * { margin: 0; padding: 0; box-sizing: border-box; }
  html, body {
    width: 1093px;
    height: 1200px;
    overflow: hidden;
    background: var(--page-bg);
  }
  .canvas {
    position: relative;
    width: 1093px;
    height: 1200px;
  }
  .card {
    position: absolute;
    left: 265px;
    width: 579px;
    height: 357px;
    box-shadow: 2px 3px 6px rgba(0, 0, 0, 0.6);
  }
  .card--front { top: 226px; background: var(--card-front); }
  .card--back { top: 620px; background: var(--card-back); }
  .card__frame {
    position: absolute;
    inset: 15px;
    border: 1px solid var(--gold-line);
  }
  .card__content {
    position: absolute;
    inset: 0;
    display: flex;
    flex-direction: column;
    align-items: center;
    justify-content: center;
    text-align: center;
    color: var(--gold-text);
  }
  .person-name {
    font-family: "Montserrat", sans-serif;
    font-weight: 800;
    font-size: 20px;
    letter-spacing: 0.2px;
    line-height: 1;
    margin-top: -2px;
  }
  .person-role {
    font-family: "Arimo", sans-serif;
    font-size: 16.5px;
    line-height: 1;
    margin-top: 3px;
  }
  .divider {
    width: 94px;
    height: 1px;
    background: var(--gold-line);
  }
  .divider--top { margin-top: 16px; margin-bottom: 18px; }
  .divider--bottom { margin-top: 16px; }
  .contact-list {
    list-style: none;
    font-family: "Lato", sans-serif;
    font-size: 16.5px;
    line-height: 21px;
  }
  .brand-mark {
    width: 58px;
    height: 58px;
    border-radius: 50%;
    background: var(--gold-bright);
    margin-top: -8px;
  }
  .brand-name {
    font-family: "Montserrat", sans-serif;
    font-weight: 800;
    font-size: 36px;
    line-height: 1;
    margin-top: 14px;
    color: var(--gold-bright);
  }
</style>
</head>
<body>
  <main class="canvas">
    <section class="card card--front" aria-label="Business card front">
      <div class="card__frame"></div>
      <div class="card__content">
        <h1 class="person-name">MARCUS HALE</h1>
        <p class="person-role">Managing Director</p>
        <div class="divider divider--top"></div>
        <ul class="contact-list">
          <li>M: (555) NOW-BOLT</li>
          <li>E: info@voltamedica.example</li>
          <li>W: www.voltamedica.example</li>
        </ul>
        <div class="divider divider--bottom"></div>
      </div>
    </section>

    <section class="card card--back" aria-label="Business card back">
      <div class="card__frame"></div>
      <div class="card__content">
        <div class="brand-mark" aria-hidden="true"></div>
        <p class="brand-name">Volta Medica</p>
      </div>
    </section>
  </main>
</body>
</html>
```